Tessbury Pure Twist Label

We are looking for a label for our blueberry vodka and lemonade ready-to-drink cocktail. we would like the ingredients (vodka, lemon juice, cane sugar, blueberries) discretely displayed on the label. We would also like 15% alc/vol (30 proof) on the label. The label is for a 12-ounce slim can. We would also like the Surgeon Generals warning ion the label

Target Market(s)

Spike seltzer and ready to drink cocktail drinkers

Font styles to use
Decorative

Requirements
Must have
• Surgeon General warning, 15% alc/vol (30 proof) 12 ounces., Ingredients

```html
<!DOCTYPE html>
<html lang="en">
<head>
<meta charset="utf-8">
<title>Tessbury Pure Twist – Blueberry Vodka and Lemonade Label</title>
<link rel="stylesheet" href="https://fonts.googleapis.com/css2?family=Big+Shoulders+Display:wght@800&family=Advent+Pro:wght@400&family=Alegreya+SC:wght@800&family=Saira+Condensed:wght@500&family=Oswald:wght@500&display=swap">
<style>
  :root {
    --page: #ffffff;
    --lemon-light: #fbf3b4;
    --lemon: #efd66a;
    --lemon-deep: #c9a92a;
    --navy: #1e3c96;
    --sky-text: #5ea2cc;
    --blue-deep: #1c4f94;
    --blue-mid: #3f86c3;
    --blue-light: #6aacd8;
    --silver: #d7dde3;
    --white: #ffffff;
    --fruit-blue: #2a68b3;
    --fruit-yellow: #f4dc55;
    --fruit-green: #6cae3c;
  }
  html, body {
    margin: 0;
    padding: 0;
    width: 1200px;
    height: 1000px;
    overflow: hidden;
    background: var(--page);
  }
  .canvas {
    position: relative;
    width: 1200px;
    height: 1000px;
  }
  .label {
    position: absolute;
    left: 428px;
    top: 150px;
    width: 362px;
    height: 760px;
    overflow: hidden;
  }
  .label-bg {
    position: absolute;
    inset: 0;
  }
  .centered {
    position: absolute;
    left: 0;
    width: 100%;
    text-align: center;
    margin: 0;
  }
  .category {
    top: 37px;
    font-family: "Advent Pro", sans-serif;
    font-size: 25px;
    letter-spacing: 2.5px;
    color: var(--navy);
  }
  .brand {
    top: 68px;
    font-family: "Big Shoulders Display", sans-serif;
    font-weight: 800;
    font-size: 90px;
    line-height: 90px;
    letter-spacing: 2px;
    color: var(--navy);
  }
  .brand-line {
    top: 168px;
    font-family: "Advent Pro", sans-serif;
    font-size: 46px;
    line-height: 50px;
    letter-spacing: 1px;
    color: var(--sky-text);
  }
  .fruit-art {
    position: absolute;
    left: 98px;
    top: 248px;
    width: 132px;
    height: 96px;
  }
  .flavour {
    top: 400px;
    font-family: "Alegreya SC", serif;
    font-weight: 800;
    font-size: 43px;
    line-height: 46px;
    color: var(--white);
    text-shadow: 0 1px 2px rgba(0, 0, 40, 0.35);
  }
  .ingredients {
    top: 542px;
    font-family: "Saira Condensed", sans-serif;
    font-weight: 500;
    font-size: 17px;
    line-height: 23px;
    color: var(--white);
  }
  .warning {
    top: 626px;
    left: 64px;
    width: 234px;
    font-family: "Oswald", sans-serif;
    font-weight: 500;
    font-size: 8px;
    line-height: 14px;
    color: var(--white);
  }
  .contents {
    top: 719px;
    font-family: "Saira Condensed", sans-serif;
    font-weight: 500;
    font-size: 18px;
    color: var(--white);
  }
</style>
</head>
<body>
<div class="canvas">
  <section class="label" aria-label="Tessbury Pure Twist blueberry vodka and lemonade can label">
    <svg class="label-bg" width="362" height="760" viewBox="0 0 362 760" aria-hidden="true">
      <defs>
        <linearGradient id="lemonBand" x1="0" y1="0" x2="1" y2="0">
          <stop offset="0" stop-color="var(--lemon-deep)"/>
          <stop offset="0.25" stop-color="var(--lemon)"/>
          <stop offset="0.5" stop-color="var(--lemon-light)"/>
          <stop offset="0.75" stop-color="var(--lemon)"/>
          <stop offset="1" stop-color="var(--lemon-deep)"/>
        </linearGradient>
        <linearGradient id="blueBody" x1="0" y1="0" x2="1" y2="0">
          <stop offset="0" stop-color="var(--blue-deep)"/>
          <stop offset="0.5" stop-color="var(--blue-light)"/>
          <stop offset="1" stop-color="var(--blue-deep)"/>
        </linearGradient>
      </defs>
      <rect x="0" y="0" width="362" height="760" fill="url(#lemonBand)"/>
      <path d="M0 268 Q181 340 362 268 L362 760 L0 760 Z" fill="url(#blueBody)"/>
      <path d="M0 262 Q181 334 362 262" fill="none" stroke="var(--silver)" stroke-width="9"/>
    </svg>

    <p class="centered category">READY-TO-DRINK COCKTAIL</p>
    <h1 class="centered brand">TESSBURY</h1>
    <p class="centered brand-line">PURE TWIST</p>

    <svg class="fruit-art" viewBox="0 0 132 96" role="img" aria-label="Illustration of blueberries with a lemon slice and green leaves">
      <rect x="0" y="0" width="132" height="96" rx="40" fill="var(--fruit-blue)" opacity="0.85"/>
    </svg>

    <h2 class="centered flavour">BLUEBERRY VODKA<br>AND LEMONADE</h2>

    <p class="centered ingredients">INGREDIENTS: VODKA, LEMON JUICE,<br>CANE SUGAR, BLUEBERRIES</p>

    <p class="centered warning">GOVERNMENT WARNING: (1) ACCORDING TO THE SURGEON GENERAL, WOMEN SHOULD NOT DRINK ALCOHOLIC BEVERAGES DURING PREGNANCY BECAUSE OF THE RISK OF BIRTH DEFECTS. (2) CONSUMPTION OF ALCOHOLIC BEVERAGES IMPAIRS YOUR ABILITY TO DRIVE A CAR OR OPERATE MACHINERY, AND MAY CAUSE HEALTH PROBLEMS.</p>

    <p class="centered contents">15% ALC/VOL (30 PROOF) 12 OUNCES</p>
  </section>
</div>
</body>
</html>
```